The name of the company is Dorvane Holdings, LLC. I would like a business card with a logo.

On the top left, I would like a logo design of a crown and I would like Dorvane over the top of the crown while Investments on the bottom. Please see attached files as an example of crown and positioning of Dorvane Holdings. Then I would like the letters DH in the middle(see picture).

Colors

Designer to choose colors to be used in the design.

```html
<!DOCTYPE html>
<html lang="en">
<head>
<meta charset="utf-8">
<title>Dorvane Holdings, LLC — Business Card</title>
<link rel="stylesheet" href="https://fonts.googleapis.com/css2?family=Bebas+Neue&family=Lato:wght@400;700&display=swap">
<style>
  :root {
    --stage: #e7e3de;
    --card-light: #ffffff;
    --card-dark: #3a3a3a;
    --ink: #2e2e2e;
    --ink-soft: #3c3c3c;
    --paper-ink: #ffffff;
    --watermark: #e6e6e6;
    --shadow: rgba(0, 0, 0, 0.35);
  }
  * { margin: 0; padding: 0; box-sizing: border-box; }
  html, body { width: 1200px; height: 900px; overflow: hidden; }
  body { background: var(--stage); position: relative; font-family: "Lato", sans-serif; }

  .card { position: absolute; overflow: hidden; box-shadow: 3px 4px 6px var(--shadow); }
  .card--front { left: 330px; top: 90px; width: 555px; height: 343px; background: var(--card-light); color: var(--ink); }
  .card--back  { left: 330px; top: 470px; width: 558px; height: 342px; background: var(--card-dark); color: var(--paper-ink); }

  .watermark-disc { position: absolute; left: 505px; top: 0; width: 0; height: 0; }
  .watermark-disc svg { position: absolute; left: 0; top: 0; }

  .brand-mark { position: absolute; display: flex; flex-direction: column; align-items: center; gap: 8px; }
  .brand-mark__dot { width: 56px; height: 56px; border-radius: 50%; background: currentColor; }
  .brand-mark__name { font-family: "Bebas Neue", sans-serif; font-size: 22px; letter-spacing: 0.5px; line-height: 1; }
  .card--front .brand-mark { left: 80px; top: 40px; width: 72px; }
  .card--back .brand-mark { left: 243px; top: 88px; width: 72px; }

  .company-title { position: absolute; font-family: "Bebas Neue", sans-serif; line-height: 1; white-space: nowrap; }
  .card--front .company-title { left: 25px; top: 157px; font-size: 24px; }
  .card--back .company-title { left: 0; width: 100%; text-align: center; top: 232px; font-size: 27px; }

  .holder { position: absolute; right: 31px; top: 57px; text-align: right; }
  .holder__name { font-family: "Bebas Neue", sans-serif; font-size: 24px; line-height: 1; }
  .holder__role { font-size: 15px; line-height: 1.2; color: var(--ink-soft); }

  .contact { position: absolute; left: 25px; top: 201px; font-size: 15.5px; line-height: 20px; color: var(--ink-soft); }
  .contact__org { font-weight: 700; }
  .contact__lines { margin-bottom: 9px; }
  .contact__row { display: flex; align-items: center; gap: 3px; }
  .contact__row svg { width: 12px; height: 12px; fill: var(--ink-soft); }
</style>
</head>
<body>

  <section class="card card--front" aria-label="Business card front">
    <div class="watermark-disc" aria-hidden="true">
      <svg width="420" height="420" viewBox="0 0 420 420" style="left:-120px;top:0">
        <circle cx="190" cy="200" r="190" fill="var(--watermark)" opacity="0.55"/>
      </svg>
    </div>

    <div class="brand-mark">
      <span class="brand-mark__dot" aria-hidden="true"></span>
      <span class="brand-mark__name">Dorvane</span>
    </div>

    <h1 class="company-title">Dorvane Holdings, LLC</h1>

    <div class="holder">
      <p class="holder__name">Taren Oakfield, MBA</p>
      <p class="holder__role">Founder / CEO</p>
    </div>

    <address class="contact" style="font-style:normal">
      <div class="contact__lines">
        <p class="contact__org">Dorvane Holdings, LLC</p>
        <p>412 Harbor Crest Drive Suite 300</p>
        <p>Linden Vale, CA 90311</p>
      </div>
      <p class="contact__row">
        <svg viewBox="0 0 24 24" aria-hidden="true"><path d="M6.6 10.8a15.1 15.1 0 0 0 6.6 6.6l2.2-2.2c.3-.3.7-.4 1-.2 1.1.4 2.3.6 3.6.6.6 0 1 .4 1 1V20c0 .6-.4 1-1 1A17 17 0 0 1 3 4c0-.6.4-1 1-1h3.5c.6 0 1 .4 1 1 0 1.3.2 2.5.6 3.6.1.3 0 .7-.2 1z"/></svg>
        (555) 014-2290
      </p>
      <p class="contact__row">
        <svg viewBox="0 0 24 24" aria-hidden="true"><path d="M2 5h20v14H2z M2 5l10 8 10-8" fill="var(--ink-soft)"/><path d="M3 6l9 7 9-7" fill="none" stroke="#fff" stroke-width="1.6"/></svg>
        dorvaneholdings@mailbox.com
      </p>
    </address>
  </section>

  <section class="card card--back" aria-label="Business card back">
    <div class="brand-mark">
      <span class="brand-mark__dot" aria-hidden="true"></span>
      <span class="brand-mark__name">Dorvane</span>
    </div>
    <h2 class="company-title">Dorvane Holdings, LLC</h2>
  </section>

</body>
</html>
```